Business Card for Kinesiologist Practitioner

I need a logo and business card designing for a Kinesiologist Practitioner. I would like the card to be double sided. The look and feel of the logo and graphics should depict natural healing and well being. I would like a modern, fresh and contemporary design with a professional style. I have attached some logos and business cards that I liek from other natural health practitioners. I have also attached some logos that I like and a mock up of the business card style. Please however use your own creative input to change any element as you feel appropriate.

I have used the strap line "Quiet Renewal" which I would like underneath the logo. For the logo I like natural objects and possibly with 3 elements in the design as the course I have studied follows a "Open Arc " healing concept (mind, body, soul). Maybe a tree or flower with 3 elements and a representation or suggestion of the human body somehow. You will see from the logos i have uploaded

Industry/Entity Type

Business

Contact Information for Business Card

Please see the mock up attached.

Font styles to use
Serif
Sans Serif

Colors
faa54b
acd036
fbee3d
85cae6

Requirements
Must have
• Note the colours are just suggested colours. Please us your own creative licence.

```html
<!DOCTYPE html>
<html lang="en">
<head>
<meta charset="utf-8">
<title>Quiet Renewal – Business Card</title>
<link href="https://fonts.googleapis.com/css2?family=Quicksand:wght@400&family=Open+Sans:wght@400;700&display=swap" rel="stylesheet">
<style>
  :root {
    --navy: #241f63;
    --white: #ffffff;
    --backdrop: #2b2b2b;
    --rule: #4a4690;
  }
  * { margin: 0; padding: 0; box-sizing: border-box; }
  html, body { width: 1200px; height: 1200px; overflow: hidden; }
  body {
    background: var(--backdrop);
    position: relative;
    font-family: "Open Sans", sans-serif;
  }
  .card {
    position: absolute;
    left: 250px;
    width: 700px;
    height: 400px;
    border-radius: 28px;
    overflow: hidden;
  }
  /* Back side */
  .card-back {
    top: 150px;
    background: var(--navy);
    color: var(--white);
    display: flex;
    flex-direction: column;
    align-items: center;
    justify-content: center;
    gap: 34px;
  }
  .brand-dot {
    width: 150px;
    height: 150px;
    border-radius: 50%;
    background: var(--white);
  }
  .brand-name {
    font-family: "Quicksand", sans-serif;
    font-weight: 400;
    font-size: 40px;
    letter-spacing: 1px;
  }
  /* Front side */
  .card-front {
    top: 650px;
    background: var(--white);
    color: var(--navy);
  }
  .front-wave {
    position: absolute;
    left: 0; bottom: 0;
    width: 700px; height: 400px;
  }
  .front-mark {
    position: absolute;
    left: 70px;
    top: 95px;
    width: 190px;
    height: 190px;
    border-radius: 50%;
    background: var(--navy);
  }
  .front-info {
    position: absolute;
    right: 48px;
    top: 40px;
    width: 360px;
    text-align: right;
  }
  .front-brand {
    font-family: "Quicksand", sans-serif;
    font-weight: 400;
    font-size: 40px;
    letter-spacing: 1px;
    margin-bottom: 28px;
  }
  .person-name {
    font-size: 24px;
    font-weight: 700;
  }
  .person-name .credentials {
    font-size: 17px;
    font-weight: 400;
  }
  .divider {
    height: 1px;
    background: var(--rule);
    margin: 10px 0 6px;
  }
  .person-role {
    font-size: 15px;
    margin-bottom: 26px;
  }
  .contact-list { list-style: none; }
  .contact-item {
    display: flex;
    justify-content: flex-end;
    align-items: center;
    gap: 10px;
    font-size: 16px;
    line-height: 1.6;
  }
  .contact-icon {
    width: 20px;
    height: 20px;
    flex: none;
  }
</style>
</head>
<body>

  <section class="card card-back">
    <div class="brand-dot"></div>
    <div class="brand-name">Quiet Renewal</div>
  </section>

  <section class="card card-front">
    <svg class="front-wave" viewBox="0 0 700 400" aria-hidden="true">
      <path d="M0 300 C 120 290, 220 330, 340 360 C 460 390, 580 370, 700 330 L700 400 L0 400 Z" fill="var(--navy)"/>
    </svg>

    <div class="front-mark"></div>

    <div class="front-info">
      <div class="front-brand">Quiet Renewal</div>
      <div class="person-name">Mara Lindell <span class="credentials">Dip. Cert.</span></div>
      <div class="divider"></div>
      <div class="person-role">Kinesiologist</div>
      <ul class="contact-list">
        <li class="contact-item">
          <span>0400 555 018</span>
          <svg class="contact-icon" viewBox="0 0 20 20" aria-hidden="true">
            <circle cx="10" cy="10" r="10" fill="var(--navy)"/>
            <path d="M7 5.5l2 2-1 1.3c.6 1.3 1.6 2.3 2.9 2.9l1.3-1 2 2-1.2 1.6c-3.7-.4-6.8-3.5-7.2-7.2z" fill="var(--white)"/>
          </svg>
        </li>
        <li class="contact-item">
          <span>maralindell@mailbox.com</span>
          <svg class="contact-icon" viewBox="0 0 20 20" aria-hidden="true">
            <circle cx="10" cy="10" r="10" fill="var(--navy)"/>
            <rect x="5" y="6.5" width="10" height="7" fill="none" stroke="var(--white)" stroke-width="1.2"/>
            <path d="M5 6.5l5 4 5-4" fill="none" stroke="var(--white)" stroke-width="1.2"/>
          </svg>
        </li>
      </ul>
    </div>
  </section>

</body>
</html>
```